Design Request: Social Media/Banner Ads for Beer Brand
Dimensions: 1028x1028 pixels
Final Format: Layered Vectors in AI, EPS, JPG and PNG

About Tolvane
Founded in 2015, Tolvane Malting Company is North America's first brewery solely dedicated to producing non-alcoholic craft beer. Thanks to a proprietary brewing process, Tolvane creates
award-winning craft beer styles that taste exactly like their alcoholic counterparts.

Brand Mission
In 2015, Tolvane was founded with a simple mission: to create a beer anyone could drink. One that was crafted for both the serious beer enthusiast and the average drinker who likes to be included in social settings. One that could be consumed individually or in large quantities, without the negative impact alcohol has on the human body. When it matters most – whether outside on an adventure or just getting together with friends in the backyard.

Brand Voice
Tolvane is a community of avid beer drinkers who like the taste of beer without the impact of alcohol. Tolvane is about making choices, and the freedom to determine your own path, being authentic to one-self, embracing life to the fullest, one simple moment at a time. Like
drinking a non-alcoholic beer with your friends when you don’t drink alcohol.

Brand Message
Our core message has truly remained the same with a focus on inclusivity, authenticity, and celebrating the the passion of those who make, sell and buy our products. Tolvane is about celebrating the little freedoms, the choices we make every day, the moments in times that
fill our days and give us purpose. Whether you spend time catching up with an old friend, getting together with others to celebrate a milestone, trying out a new hobby, or going thru the motions of life as one would know it, Tolvane is about making those moments count.

Additional Information
Please refer to the brand style guide to view the mood boards and for design specifications. Also, attached is the press kit for additional brand information.

Target Market(s)

- Beer for celebrating moments of personal accomplishment
- Beer for men and women living the American dream
- Beer for the healthy, social and active lifestyle
- Beer for those who value premium non-alcoholic beer

Industry/Entity Type

Consumer

Font styles to use
Serif

Requirements
Must have
• Please refer to the brand style guide to see the mood boards, photography, and design specifications. We need high quality, modern designs for paid ads placed on facebook, Instagram, and google ads.

Square ad size, using brand guidelines, one call to action on the design using value prop from the press kit and brand guide messaging
Nice to have
• assuming you can use a combination of stock imagery with resources available in the attached documents to give us a high-end, clean, modern design, depicting our premium, lifestyle-focused, non-alcoholic beer brand.
Should not have
• please refer to brand guidelines

```html
<!DOCTYPE html>
<html lang="en">
<head>
<meta charset="utf-8">
<title>Tolvane — Drink Ad</title>
<link href="https://fonts.googleapis.com/css2?family=Montserrat:wght@800&family=Mr+Dafoe&display=swap" rel="stylesheet">
<style>
  :root {
    --paper: #ffffff;
    --sky-top: #c7b39c;
    --sky-glow: #e9a456;
    --horizon: #b0682a;
    --field: #5a3a1e;
    --ground: #1f160e;
    --brand-teal: #1d4857;
    --headline: #ffffff;
    --accent-gold: #f1bb5e;
  }
  html, body {
    margin: 0;
    padding: 0;
    width: 1200px;
    height: 1200px;
    overflow: hidden;
    background: var(--paper);
  }
  .ad {
    position: relative;
    width: 1200px;
    height: 1200px;
    background: var(--paper);
    overflow: hidden;
  }
  .ad__photo {
    position: absolute;
    inset: 21px;
    z-index: 0;
    background:
      radial-gradient(circle at 62% 32%, rgba(255, 226, 150, 0.9) 0, rgba(255, 190, 90, 0.5) 12%, rgba(233, 164, 86, 0) 35%),
      linear-gradient(180deg, var(--sky-top) 0%, var(--sky-glow) 28%, var(--horizon) 40%, var(--field) 58%, var(--ground) 100%);
  }
  .ad__brand {
    position: absolute;
    z-index: 3;
    left: 46px;
    top: 56px;
    margin: 0;
    font-family: "Montserrat", sans-serif;
    font-weight: 800;
    font-size: 86px;
    line-height: 1;
    letter-spacing: 1px;
    color: var(--brand-teal);
  }
  .ad__script {
    position: absolute;
    z-index: 1;
    left: 0;
    right: 0;
    top: 770px;
    margin: 0;
    text-align: center;
    font-family: "Mr Dafoe", cursive;
    font-size: 320px;
    line-height: 1;
    color: var(--accent-gold);
    transform: translateX(-22px);
    pointer-events: none;
  }
  .ad__headline {
    position: absolute;
    z-index: 2;
    left: 0;
    right: 0;
    top: 546px;
    margin: 0;
    text-align: center;
    font-family: "Montserrat", sans-serif;
    font-weight: 800;
    font-size: 68px;
    line-height: 59px;
    color: var(--headline);
    transform: translateX(-8px);
  }
  .ad__headline span { display: block; }
  .ad__tail {
    position: absolute;
    z-index: 2;
    left: 0;
    right: 0;
    top: 1069px;
    margin: 0;
    text-align: center;
    font-family: "Montserrat", sans-serif;
    font-weight: 800;
    font-size: 68px;
    line-height: 1;
    color: var(--headline);
    transform: translateX(-8px);
  }
</style>
</head>
<body>
  <main class="ad">
    <div class="ad__photo" role="img" aria-label="Two hands clinking amber beer bottles against a golden sunset over a wheat field"></div>
    <p class="ad__brand">Tolvane</p>
    <p class="ad__script" aria-hidden="true">Drink</p>
    <h1 class="ad__headline">
      <span>DRINKING</span>
      <span>A NON-ALCOHOLIC</span>
      <span>BEER WITH YOUR</span>
      <span>FRIENDS WHEN</span>
      <span>YOU DON’T</span>
    </h1>
    <p class="ad__tail">ALCOHOL</p>
  </main>
</body>
</html>
```